UI Mockup For Online Scheduling Software

11.01.2018 - Brief Update:
The brief has not changed but the summary below as being added to aid designers.

- New file added "Updated 11.01.2018 - Individual Box" to clarify the sections. Specifically the primary tag section
- Improve on the current styling
- Consider changing the section layout to maximise the number of blocks displayed on screen (The sections dont not need to be stacked like the current version.
- The design is for the application running on a desktop PC with 16:9 screen aspect
- The design styling/layout should not look like the current version
- You may use the application to get an understanding of its workings at this link....https://marlowtesk.brivanlabs.com.au/
- Think outside the box....use your creative flare and show me something different to the current app (style and layout)

There are already some good submissions so closer to the deadline I will increase the budget and award $$$ to 1st and 2nd. The winner will be chosen to directly work on the remaining aspects of this application (setting page, mobile design, dashboard etc). The next design project associated to this application will be 10 time bigger than this one.

Good Luck Designers

*************************************************************
Redesign the user interface to make more efficient use of the screen real estate.

The software works by adding (Drag & Drop) Project Blocks to a Date Section. Then tags are added (Drag & Drop) to the block section below the header, and then resources are added to the block section below the tags.
Each block has 4 main sections that are stacked vertically:

1. Header - Displays Title and Address
2. Tags - Displays tags, maximum of 6 tags
3. Resources - Displays resources, maximum of 10 resources, NOTE: this section can be hidded.
4. Footer - Display basic stats (eg. 3 Resources assigned)

It is critical that as many block (20-30) as possible for a single date can be visible on screen.

The following criteria must be considered when mocking up layout:
1. Font Type, size, colour and emphasis
2. Block Colour/Shading, borders ect
3. Section Layout within the block (stacking & Alignment)
4. Mock ups to show scaled layout of blocks in both the open state and Closed State.
5. Mock up to display a minimum of 20 blocks.
6. Create a variation of your design that adds a 5th section. This will display the first tag only:
1. Header - Always Visible
2. Primary Tag - Always Visible
3. Secondary Tags - Can be hidden
4. Resources - Can be Hidden
5. Footer - Can be Hidden

Please be creative with your design and layout. I like a clean, minimalist design.
At this stage CSS file will not be required but would be benificial
Updates

Designs look the same

Target Market(s)

N/A

Industry/Entity Type

Software

Number of Pages Required

1 page

Font styles to use
Other font styles liked:
• Designers Choice

Colors

Designer to choose colors to be used in the design.

Requirements
Must have
• Variation to current layout and style
Should not have
• Same styling and layout as current design

```html
<!DOCTYPE html>
<html lang="en">
<head>
<meta charset="utf-8">
<title>Sprayform Australia – Schedule</title>
<link href="https://fonts.googleapis.com/css2?family=Open+Sans:wght@400;600;700&display=swap" rel="stylesheet">
<style>
:root{
  --topbar:#0c4585;
  --sidebar:#0b355f;
  --sidebar-line:#0e416f;
  --accent:#f07a2a;
  --filter:#2ea6e2;
  --board:#e2e2e2;
  --card:#f4f4f4;
  --text:#333;
  --muted:#888;
  --tag-grey:#ececec;
  --tag-blue:#cfe3f7;
  --tag-yellow:#fffb00;
  --tag-orange:#f8b483;
  --tag-green:#c9f3c4;
  --tag-cream:#fcf3c0;
  --tag-lilac:#cfcbe4;
  --link:#2a7fc4;
}
*{box-sizing:border-box;margin:0;padding:0}
html,body{width:1200px;height:771px;overflow:hidden;background:#fff;font-family:"Open Sans",Arial,sans-serif;color:var(--text)}
ul{list-style:none}
.topbar{position:absolute;left:0;top:0;width:1200px;height:33px;background:var(--topbar)}
.brand{position:absolute;left:10px;top:8px;color:#fff;font-weight:700;font-size:13px;letter-spacing:-.2px}
.user{position:absolute;right:36px;top:8px;text-align:right;color:#fff;line-height:1}
.user small{display:block;font-size:4.5px}
.user strong{font-size:6.5px;font-weight:600}
.avatar{position:absolute;right:10px;top:7px;width:19px;height:19px;border-radius:50%;background:linear-gradient(#c9a58a,#6d5a4e)}
.sidebar{position:absolute;left:0;top:33px;width:94px;height:738px;background:var(--sidebar)}
.nav li{height:26.6px;border-bottom:1px solid var(--sidebar-line);display:flex;align-items:center;padding-left:11px;color:#fff;font-size:7px;font-weight:600;letter-spacing:.2px}
.nav li::before{content:"";width:7px;height:6px;background:#fff;border-radius:1px;margin-right:7px}
.filters{position:absolute;left:103px;top:44px;width:1087px;height:59px;background:var(--filter);padding:6px 8px}
.filters h2{font-size:6px;font-weight:400;color:#fff}
.fields{display:flex;gap:6px;margin-top:5px}
.field{width:84px;height:16px;background:#fff;border-radius:1px;font-size:4.6px;color:#555;padding:0 6px;display:flex;align-items:center;justify-content:space-between}
.field::after{content:"";width:5px;height:4px;background:#999}
.field.select::after{width:0;height:0;background:none;border:2px solid transparent;border-top:2.5px solid #555;margin-top:2px}
.quick{display:flex;gap:4px;margin-top:4px}
.quick span{border:1px solid #c7e6f7;color:#fff;font-size:4.6px;height:11px;padding:0 5px;display:flex;align-items:center;border-radius:1px}
.dayline{position:absolute;left:103px;top:110px;width:1087px;height:20px}
.day{position:absolute;left:0;top:0;font-size:7px;color:var(--link)}
.day::before{content:"";display:inline-block;width:5px;height:5px;background:var(--link);margin-right:4px}
.note{position:absolute;left:0;top:11px;font-size:4.6px;color:var(--link)}
.meta{position:absolute;top:2px;font-size:4.6px;color:#666}
.board{position:absolute;left:103px;top:133px;width:1087px;height:601px;background:var(--board);padding:15px 12px;display:grid;grid-template-columns:repeat(10,90px);grid-auto-rows:179px;column-gap:18px;row-gap:18px}
.block{background:var(--card);border-bottom:2px solid var(--accent);position:relative}
.block header{background:#fff;height:24px;padding:5px 4px 0}
.block h3{font-size:5.6px;font-weight:700;white-space:nowrap;overflow:hidden}
.block header p{font-size:3.3px;color:var(--muted);margin-top:1px}
.gear{position:absolute;right:8px;top:15px;width:3.5px;height:3.5px;border-radius:50%;border:1px solid #999}
.tags{height:65px;padding:5px 5px 0}
.tag,.res li{height:10.3px;font-size:3.9px;display:flex;align-items:center;padding:0 4px;margin-bottom:3px;position:relative}
.tag::before{content:"";width:4px;height:3.5px;background:#666;margin-right:5px;border-radius:1px 0 0 1px}
.tag::after,.res li::after{content:"×";position:absolute;right:4px;font-size:5px;font-weight:700;color:#444}
.tag{background:var(--tag-grey);color:#777}
.trade{background:var(--tag-blue);color:#333}
.trade::before{background:#2b5b8c}
.cream{background:var(--tag-cream);color:#777}
.lilac{background:var(--tag-lilac);color:#444}
.hot{background:var(--tag-yellow);color:#777}
.warn{background:var(--tag-orange);color:#555}
.ok{background:var(--tag-green);color:#333}
.ok::before{background:#2d8b3a}
.res{padding:1px 5px 0;height:78px}
.res li{background:#fff;border:1px solid #e4e4e4;color:#666}
.res li::before{content:"";width:3.5px;height:4px;border-radius:2px 2px 0 0;background:#777;margin-right:6px}
.res li:first-child{color:#222;font-size:4.6px}
.block footer{font-size:3.6px;color:#666;padding-left:3px}
.copy{position:absolute;left:0;width:1200px;top:748px;text-align:center;font-size:4.8px;color:#333}
.ver{position:absolute;right:6px;top:752px;font-size:4.4px}
</style>
</head>
<body>
<div class="topbar">
  <div class="brand">SPRAYFORM Australia</div>
  <div class="user"><small>Welcome</small><strong>Dale Prentice</strong></div>
  <div class="avatar" role="img" aria-label="User profile photo"></div>
</div>
<aside class="sidebar">
  <ul class="nav"><li>DASHBOARD</li><li>PROJECTS</li><li>RESOURCES</li><li>PLANTS</li><li>TAGS</li><li>CLIENTS</li></ul>
</aside>
<section class="filters">
  <h2>Filter By Date</h2>
  <div class="fields">
    <div class="field">10-01-2018</div><div class="field">24-01-2018</div>
    <div class="field select">Select Project</div><div class="field select">Select Client</div><div class="field select">Select Tag</div>
  </div>
  <div class="quick"><span>Yesterday</span><span>Today</span><span>Tomorrow</span><span>Next Week</span></div>
</section>
<div class="dayline">
  <div class="day">11-Jan-2018 (Thursday)</div>
  <div class="note">Note : The first name in Bold is the supervisor</div>
  <div class="meta" style="left:141px">Comment ▾</div>
  <div class="meta" style="left:197px">Project Assigned &nbsp;15 of 67</div>
  <div class="meta" style="left:281px">Resources scheduled 50 of 55</div>
</div>
<main class="board">
<!-- row 1 -->
<article class="block"><header><h3>21356 - KLT Haddon east - 127d</h3><p>KLT - Pembury St. Hollowfield</p><span class="gear"></span></header><ul class="tags"><li class="tag trade">Trade : Sprayform</li><li class="tag">Task : Piled Walls</li><li class="tag">Start 6:45 am</li><li class="tag ok">Confirmed</li></ul><ul class="res"><li>Benny K</li><li>Marco L</li><li>Sam P</li></ul><footer>3 Resources, 0 Plant Assigned</footer></article>
<article class="block"><header><h3>21485 - Ashvale</h3><p>KLT - Pembury St. Hollowfield</p><span class="gear"></span></header><ul class="tags"><li class="tag trade">Trade : Sprayform</li><li class="tag">Task : Piled Walls</li><li class="tag">Start 6:45 am</li><li class="tag ok">Confirmed</li></ul><ul class="res"><li>Benny K</li><li>Marco L</li><li>Sam P</li><li>Ridgey</li><li>Holly</li></ul><footer>3 Resources, 0 Plant Assigned</footer></article>
<article class="block"><header><h3>21487 - Riverside Park</h3><p>KLT - Pembury St. Hollowfield</p><span class="gear"></span></header><ul class="tags"><li class="tag trade">Trade : Sprayform</li><li class="tag">Task : Piled Walls</li><li class="tag">Start 6:45 am</li><li class="tag ok">Confirmed</li></ul><ul class="res"><li>Benny K</li><li>Marco L</li></ul><footer>3 Resources, 0 Plant Assigned</footer></article>
<article class="block"><header><h3>NLK - 21299 - R4k</h3><p>KLT - Pembury St. Hollowfield</p><span class="gear"></span></header><ul class="tags"><li class="tag trade">Trade : Sprayform</li><li class="tag hot">Task : Piled Walls</li><li class="tag warn">Start 6:45 am</li><li class="tag ok">Confirmed</li></ul><ul class="res"><li>Benny K</li><li>Marco L</li><li>Sam P</li></ul><footer>3 Resources, 0 Plant Assigned</footer></article>
<article class="block"><header><h3>214847 - Northgate Clinic</h3><p>KLT - Pembury St. Hollowfield</p><span class="gear"></span></header><ul class="tags"><li class="tag trade">Trade : Sprayform</li><li class="tag">Task : Piled Walls</li><li class="tag">Start 6:45 am</li><li class="tag ok">Confirmed</li></ul><ul class="res"><li>Benny K</li><li>Marco L</li><li>Sam P</li></ul><footer>3 Resources, 0 Plant Assigned</footer></article>
<article class="block"><header><h3>21372 - Wattle Ridge</h3><p>KLT - Pembury St. Hollowfield</p><span class="gear"></span></header><ul class="tags"><li class="tag trade">Trade : Sprayform</li><li class="tag">Task : Piled Walls</li><li class="tag">Start 6:45 am</li><li class="tag ok">Confirmed</li></ul><ul class="res"><li>Benny K</li><li>Marco L</li><li>Sam P</li></ul><footer>3 Resources, 0 Plant Assigned</footer></article>
<article class="block"><header><h3>21472 -Rowan Hill</h3><p>KLT - Pembury St. Hollowfield</p><span class="gear"></span></header><ul class="tags"><li class="tag cream">Trade : Sprayform</li><li class="tag">Task : Piled Walls</li><li class="tag">Start 6:45 am</li><li class="tag ok">Confirmed</li></ul><ul class="res"><li>Benny K</li><li>Marco L</li><li>Sam P</li></ul><footer>3 Resources, 0 Plant Assigned</footer></article>
<article class="block"><header><h3>21387 -Merrivale</h3><p>KLT - Pembury St. Hollowfield</p><span class="gear"></span></header><ul class="tags"><li class="tag cream">Trade : Sprayform</li><li class="tag">Task : Piled Walls</li><li class="tag">Start 6:45 am</li><li class="tag ok">Confirmed</li></ul><ul class="res"><li>Benny K</li><li>Marco L</li><li>Sam P</li></ul><footer>3 Resources, 0 Plant Assigned</footer></article>
<article class="block"><header><h3>21485 - Ashvale</h3><p>KLT - Pembury St. Hollowfield</p><span class="gear"></span></header><ul class="tags"><li class="tag trade">Trade : Sprayform</li><li class="tag">Task : Piled Walls</li><li class="tag">Start 6:45 am</li><li class="tag ok">Confirmed</li></ul><ul class="res"><li>Benny K</li><li>Marco L</li><li>Sam P</li></ul><footer>3 Resources, 0 Plant Assigned</footer></article>
<article class="block"><header><h3>21356 - KLT Haddon east - 127d</h3><p>KLT - Pembury St. Hollowfield</p><span class="gear"></span></header><ul class="tags"><li class="tag trade">Trade : Sprayform</li><li class="tag">Task : Piled Walls</li><li class="tag">Start 6:45 am</li><li class="tag ok">Confirmed</li></ul><ul class="res"><li>Benny K</li><li>Marco L</li><li>Sam P</li></ul><footer>3 Resources, 0 Plant Assigned</footer></article>
<!-- row 2 -->
<article class="block"><header><h3>NLK - 21299 - R4k</h3><p>KLT - Pembury St. Hollowfield</p><span class="gear"></span></header><ul class="tags"><li class="tag trade">Trade : Sprayform</li><li class="tag hot">Task : Piled Walls</li><li class="tag warn">Start 6:45 am</li><li class="tag ok">Confirmed</li></ul><ul class="res"><li>Benny K</li><li>Marco L</li><li>Sam P</li></ul><footer>3 Resources, 0 Plant Assigned</footer></article>
<article class="block"><header><h3>21485 - Vestibulum</h3><p>KLT - Pembury St. Hollowfield</p><span class="gear"></span></header><ul class="tags"><li class="tag trade">Trade : Sprayform</li><li class="tag">Task : Piled Walls</li><li class="tag">Start 6:45 am</li><li class="tag ok">Confirmed</li></ul><ul class="res"><li>Benny K</li><li>Marco L</li><li>Sam P</li><li>Ridgey</li><li>Holly</li></ul><footer>3 Resources, 0 Plant Assigned</footer></article>
<article class="block"><header><h3>21487 - Pellentesque</h3><p>KLT - Pembury St. Hollowfield</p><span class="gear"></span></header><ul class="tags"><li class="tag trade">Trade : Sprayform</li><li class="tag">Task : Piled Walls</li><li class="tag">Start 6:45 am</li><li class="tag ok">Confirmed</li></ul><ul class="res"><li>Benny K</li><li>Marco L</li></ul><footer>3 Resources, 0 Plant Assigned</footer></article>
<article class="block"><header><h3>21356 - Maecenas</h3><p>KLT - Pembury St. Hollowfield</p><span class="gear"></span></header><ul class="tags"><li class="tag trade">Trade : Sprayform</li><li class="tag">Task : Piled Walls</li><li class="tag">Start 6:45 am</li><li class="tag ok">Confirmed</li></ul><ul class="res"><li>Benny K</li><li>Marco L</li><li>Sam P</li></ul><footer>3 Resources, 0 Plant Assigned</footer></article>
<article class="block"><header><h3>214847 - Fusce sollicitudin</h3><p>KLT - Pembury St. Hollowfield</p><span class="gear"></span></header><ul class="tags"><li class="tag trade">Trade : Sprayform</li><li class="tag">Task : Piled Walls</li><li class="tag">Start 6:45 am</li><li class="tag ok">Confirmed</li></ul><ul class="res"><li>Benny K</li><li>Marco L</li><li>Sam P</li></ul><footer>3 Resources, 0 Plant Assigned</footer></article>
<article class="block"><header><h3>21372 - Aenean facilisis</h3><p>KLT - Pembury St. Hollowfield</p><span class="gear"></span></header><ul class="tags"><li class="tag trade">Trade : Sprayform</li><li class="tag">Task : Piled Walls</li><li class="tag">Start 6:45 am</li><li class="tag ok">Confirmed</li></ul><ul class="res"><li>Benny K</li><li>Marco L</li><li>Sam P</li></ul><footer>3 Resources, 0 Plant Assigned</footer></article>
<article class="block"><header><h3>21472 -Etiam mattis</h3><p>KLT - Pembury St. Hollowfield</p><span class="gear"></span></header><ul class="tags"><li class="tag cream">Trade : Sprayform</li><li class="tag">Task : Piled Walls</li><li class="tag">Start 6:45 am</li><li class="tag ok">Confirmed</li></ul><ul class="res"><li>Benny K</li><li>Marco L</li><li>Sam P</li></ul><footer>3 Resources, 0 Plant Assigned</footer></article>
<article class="block"><header><h3>21387 - Cras sollicitudin</h3><p>KLT - Pembury St. Hollowfield</p><span class="gear"></span></header><ul class="tags"><li class="tag cream">Trade : Sprayform</li><li class="tag">Task : Piled Walls</li><li class="tag">Start 6:45 am</li><li class="tag ok">Confirmed</li></ul><ul class="res"><li>Benny K</li><li>Marco L</li><li>Sam P</li></ul><footer>3 Resources, 0 Plant Assigned</footer></article>
<article class="block"><header><h3>21485 - Pellentesque</h3><p>KLT - Pembury St. Hollowfield</p><span class="gear"></span></header><ul class="tags"><li class="tag trade">Trade : Sprayform</li><li class="tag">Task : Piled Walls</li><li class="tag">Start 6:45 am</li><li class="tag ok">Confirmed</li></ul><ul class="res"><li>Benny K</li><li>Marco L</li><li>Sam P</li></ul><footer>3 Resources, 0 Plant Assigned</footer></article>
<article class="block"><header><h3>21356 - Vivamus eleifend</h3><p>KLT - Pembury St. Hollowfield</p><span class="gear"></span></header><ul class="tags"><li class="tag trade">Trade : Sprayform</li><li class="tag">Task : Piled Walls</li><li class="tag">Start 6:45 am</li><li class="tag ok">Confirmed</li></ul><ul class="res"><li>Benny K</li><li>Marco L</li><li>Sam P</li></ul><footer>3 Resources, 0 Plant Assigned</footer></article>
<!-- row 3 -->
<article class="block"><header><h3>21372 - Aenean facilisis</h3><p>KLT - Pembury St. Hollowfield</p><span class="gear"></span></header><ul class="tags"><li class="tag trade">Trade : Sprayform</li><li class="tag">Task : Piled Walls</li><li class="tag">Start 6:45 am</li><li class="tag ok">Confirmed</li></ul><ul class="res"><li>Benny K</li><li>Marco L</li><li>Sam P</li></ul><footer>3 Resources, 0 Plant Assigned</footer></article>
<article class="block"><header><h3>21356 - KLT Haddon east - 127d</h3><p>KLT - Pembury St. Hollowfield</p><span class="gear"></span></header><ul class="tags"><li class="tag trade">Trade : Sprayform</li><li class="tag">Task : Piled Walls</li><li class="tag">Start 6:45 am</li><li class="tag ok">Confirmed</li></ul><ul class="res"><li>Benny K</li><li>Marco L</li><li>Sam P</li></ul><footer>3 Resources, 0 Plant Assigned</footer></article>
<article class="block"><header><h3>21487 - Riverside Park</h3><p>KLT - Pembury St. Hollowfield</p><span class="gear"></span></header><ul class="tags"><li class="tag trade">Trade : Sprayform</li><li class="tag">Task : Piled Walls</li><li class="tag">Start 6:45 am</li><li class="tag ok">Confirmed</li></ul><ul class="res"><li>Benny K</li><li>Marco L</li><li>Sam P</li></ul><footer>3 Resources, 0 Plant Assigned</footer></article>
<article class="block"><header><h3>214847 - Northgate Clinic</h3><p>KLT - Pembury St. Hollowfield</p><span class="gear"></span></header><ul class="tags"><li class="tag trade">Trade : Sprayform</li><li class="tag">Task : Piled Walls</li><li class="tag">Start 6:45 am</li><li class="tag ok">Confirmed</li></ul><ul class="res"><li>Benny K</li><li>Marco L</li><li>Sam P</li></ul><footer>3 Resources, 0 Plant Assigned</footer></article>
<article class="block"><header><h3>21356 - KLT Haddon east - 127d</h3><p>KLT - Pembury St. Hollowfield</p><span class="gear"></span></header><ul class="tags"><li class="tag trade">Trade : Sprayform</li><li class="tag">Task : Piled Walls</li><li class="tag">Start 6:45 am</li><li class="tag ok">Confirmed</li></ul><ul class="res"><li>Benny K</li><li>Marco L</li><li>Sam P</li></ul><footer>3 Resources, 0 Plant Assigned</footer></article>
<article class="block"><header><h3>214847 - Northgate Clinic</h3><p>KLT - Pembury St. Hollowfield</p><span class="gear"></span></header><ul class="tags"><li class="tag trade">Trade : Sprayform</li><li class="tag">Task : Piled Walls</li><li class="tag">Start 6:45 am</li><li class="tag ok">Confirmed</li></ul><ul class="res"><li>Benny K</li><li>Marco L</li><li>Sam P</li></ul><footer>3 Resources, 0 Plant Assigned</footer></article>
<article class="block"><header><h3>21487 - Riverside Park</h3><p>KLT - Pembury St. Hollowfield</p><span class="gear"></span></header><ul class="tags"><li class="tag trade">Trade : Sprayform</li><li class="tag">Task : Piled Walls</li><li class="tag">Start 6:45 am</li><li class="tag ok">Confirmed</li></ul><ul class="res"><li>Benny K</li><li>Marco L</li><li>Sam P</li></ul><footer>3 Resources, 0 Plant Assigned</footer></article>
<article class="block"><header><h3>21465 - Pembrook</h3><p>KLT - Pembury St. Hollowfield</p><span class="gear"></span></header><ul class="tags"><li class="tag trade">Trade : Sprayform</li><li class="tag">Task : Piled Walls</li><li class="tag">Start 6:45 am</li><li class="tag ok">Confirmed</li></ul><ul class="res"><li>Benny K</li><li>Marco L</li><li>Sam P</li></ul><footer>3 Resources, 0 Plant Assigned</footer></article>
<article class="block"><header><h3>Yard Greenholm</h3><p>43 A Kestrel St</p><span class="gear"></span></header><ul class="tags"><li class="tag lilac">Trade : General</li></ul><ul class="res"><li>Frank DUNN</li></ul><footer>3 Resources, 0 Plant Assigned</footer></article>
<article class="block"><header><h3>Unavailable Resources</h3><p>Sprayform Australia - 43a Kestrel St</p><span class="gear"></span></header><ul class="tags"></ul><ul class="res"><li>Benny K</li><li>Marco L</li><li>Sam P</li><li>Marco L</li><li>Sam P</li></ul><footer>3 Resources, 0 Plant Assigned</footer></article>
</main>
<p class="copy">Copyright © 2018 Sprayform. &nbsp;All rights reserved.</p>
<span class="ver">M2</span>
</body>
</html>
```